Roaming outings business card

please see website
www.roamingoutings.comau

info needed on card
Keiran Voss
Ph
email
Adventure Riding GPS trails

please use my logo and colours off my site

Business

Keiran Voss
keiran@roamingoutings.com

```html
<!DOCTYPE html>
<html lang="en">
<head>
<meta charset="utf-8">
<title>Roaming outings – business card</title>
<link rel="stylesheet" href="https://fonts.googleapis.com/css2?family=Arimo:wght@400;700&display=swap">
<style>
  :root {
    --bg: #2a2a2a;
    --card-white: #ffffff;
    --card-black: #050505;
    --accent: #f2d21b;
    --ink: #111111;
    --muted: #6d6d6d;
    --light-text: #f2f2f2;
  }
  * { box-sizing: border-box; margin: 0; padding: 0; }
  html, body { width: 1200px; height: 750px; overflow: hidden; }
  body {
    background: var(--bg);
    font-family: "Arimo", Arial, sans-serif;
    display: flex;
    align-items: center;
    justify-content: center;
    gap: 60px;
  }
  .card {
    width: 520px;
    height: 297px;
    position: relative;
    overflow: hidden;
    box-shadow: 0 10px 30px rgba(0,0,0,0.45);
  }

  /* Front */
  .card-front {
    background: var(--card-white);
    display: flex;
    flex-direction: column;
    align-items: center;
    justify-content: center;
    gap: 14px;
  }
  .brand {
    display: flex;
    align-items: center;
    gap: 12px;
  }
  .brand-dot {
    width: 30px;
    height: 30px;
    border-radius: 50%;
    background: var(--accent);
    flex: none;
  }
  .brand-name {
    font-weight: 700;
    color: var(--ink);
    font-size: 30px;
    text-transform: uppercase;
    letter-spacing: 0.5px;
  }
  .tagline {
    color: var(--muted);
    font-size: 14px;
    letter-spacing: 0.3px;
  }

  /* Back */
  .card-back {
    display: flex;
    background: var(--card-white);
  }
  .contact-panel {
    width: 50%;
    background: var(--card-black);
    border-right: 3px solid var(--accent);
    padding: 30px 24px 26px;
    display: flex;
    flex-direction: column;
    justify-content: space-between;
  }
  .person-name {
    color: var(--accent);
    font-weight: 700;
    font-size: 18px;
  }
  .contact-list { list-style: none; display: flex; flex-direction: column; gap: 6px; }
  .contact-item {
    display: flex;
    align-items: center;
    gap: 8px;
    color: var(--light-text);
    font-size: 12px;
  }
  .contact-item svg { width: 13px; height: 13px; flex: none; }
  .brand-panel {
    width: 50%;
    display: flex;
    flex-direction: column;
    align-items: center;
    justify-content: center;
    gap: 10px;
    padding: 0 16px;
  }
  .brand-panel .brand-name { font-size: 20px; }
  .brand-panel .brand-dot { width: 20px; height: 20px; }
  .brand-panel .tagline { font-size: 11px; }
</style>
</head>
<body>
  <section class="card card-front" aria-label="Card front">
    <div class="brand">
      <span class="brand-dot"></span>
      <span class="brand-name">Roaming outings</span>
    </div>
    <p class="tagline">Adventure Riding GPS trails</p>
  </section>

  <section class="card card-back" aria-label="Card back">
    <div class="contact-panel">
      <h1 class="person-name">Keiran Voss</h1>
      <ul class="contact-list">
        <li class="contact-item">
          <svg viewBox="0 0 16 16" aria-hidden="true"><path fill="#f2d21b" d="M3.5 1.5l2.5 3-1.5 1.7c.8 1.8 2.4 3.4 4.3 4.3l1.7-1.5 3 2.5-1.3 2c-5.6.2-10.6-4.8-10.5-10.5z"/></svg>
          <span>555 0142 7788</span>
        </li>
        <li class="contact-item">
          <svg viewBox="0 0 16 16" aria-hidden="true"><rect x="1" y="3" width="14" height="10" fill="#f2d21b"/><path d="M1 3l7 6 7-6" fill="none" stroke="#050505" stroke-width="1.3"/></svg>
          <span>keiran@roamingoutings.com</span>
        </li>
        <li class="contact-item">
          <svg viewBox="0 0 16 16" aria-hidden="true"><circle cx="8" cy="8" r="7" fill="#f2d21b"/><path d="M1 8h14M8 1c-3 3.5-3 10.5 0 14M8 1c3 3.5 3 10.5 0 14" fill="none" stroke="#050505" stroke-width="1"/></svg>
          <span>www.roamingoutings.comau</span>
        </li>
      </ul>
    </div>
    <div class="brand-panel">
      <div class="brand">
        <span class="brand-dot"></span>
        <span class="brand-name">Roaming outings</span>
      </div>
      <p class="tagline">Adventure Riding GPS trails</p>
    </div>
  </section>
</body>
</html>
```